Wine label - premium, elegant & classic

We are a young husband and wife team who have worked in the wine industry for 10+ years. This year we've finally had the opportunity to make our own wine and release our own brand. Our wines are boutique and sell at a mid-premium price (we don't make a lot) so we're looking for a label design that can reflect this premium nature and mixes traditional design elements with modern reflections.

The brand is called: L&T

Reason: We've received some great design concepts over the past week which we would happily pay for, so we've decided to guarantee payment and extend the deadline to allow time for more designs to be sent through. A BIG thanks to all who have already submitted, your designs are still under consideration. Cheers, T.

A big thank you to all for taking the time to submit your beautiful designs to our project.  We now have the very tough job of looking over each of them and selecting only one.  We hope to come to a decision in the next day or two, so hopefully we won't keep you waiting too long!

Cheers, and thanks again

L&T.                                   

Target Market(s)

30 - 45 year old female and male wine drinkers

Requirements
Must have
• Can we please see two versions of the one design - one for a red wine and one for a white wine.

The front labels needs to include the following information:
1. Brand name: L&T
2. Wine varieties: Pinot Noir (red wine) and Sauvignon Blanc (white wine)
3. Vintage: 2012 for both
4. Region: Yarra Valley
5. GI: Wine of Australia (not essential to be on front label)

The back label needs to include the following:
1. The brand name: L&T
2. Variety, vintage, region and volume (the volume must be 4mm in height)
3. Room for product description - approx. 30-40 words.
4. Alcohol statement (no size restriction, pls use 12.5% ALC/VOL as example)
5. Standard drinks (no size restriction, pls use 'Approx.7.8 standard drinks' as example)
6. Sulphites statement: "Sulphites added."
7. Allergen statement: "Fined with the aid of egg and milk products and traces may remain."
8. Room for address: Approx. 20 words
9. "Wine of Australia" - no size restriction, just needs to be legible

Packaging presentation:
Pinot Noir is a red wine and Sauvignon Blanc is a white wine.
Labels for both need to be shown on premium punted burgundy bottles (pls see example: http://www.velmorapack.com/products_services/kfq_premium_burgundy_750_ml_wine_bottle.html)
Nice to have
• We would like the design to embody the following elements:
1. Classically modern
2. Clean and simple
3. Elegance
4. Restricted use of colours (ideally just black/grey, white/buff and perhaps one other)

Some design examples of what we like:
1. http://www.fernandgulls.com.au/sangiovese-tasting-notes/
2. http://quollridge.com/Wines/Quoll-Ridge-Vineyard/Range/2010-Quoll-Ridge-Single-Vineyard-Pinot-Noir-.htm
Should not have
• Preferrably won't have any photos or drawings unless you feel there is a simple symbol or image that could be used to enhance the design.

Restricted use of colours - more muted, conservative tones.

```html
<!DOCTYPE html>
<html lang="en">
<head>
<meta charset="utf-8">
<title>Packaging Design: wine label for L&amp;T</title>
<link rel="stylesheet" href="https://fonts.googleapis.com/css2?family=Didact+Gothic&family=Marcellus&family=PT+Sans+Narrow&display=swap">
<style>
  :root {
    --ink: #000000;
    --paper: #ffffff;
    --label-dark: #1f1f21;
    --label-light: #ebebec;
    --grey-deep: #2f2f2f;
    --grey-mid: #666666;
    --grey-soft: #aaaaaa;
    --grey-pale: #d3d3d3;
    --grey-mist: #f0f0f0;
    --type-dark: #333333;
    --type-muted: #7a7a7a;
  }
  * { margin: 0; padding: 0; box-sizing: border-box; }
  html, body { width: 901px; height: 1200px; overflow: hidden; background: var(--paper); }
  .sheet { position: relative; width: 901px; height: 1200px; overflow: hidden; font-family: "Marcellus", serif; }

  .sheet-title {
    position: absolute; left: 17px; top: 8px;
    font-family: "Didact Gothic", sans-serif; font-weight: 400;
    font-size: 47px; letter-spacing: 0.5px; color: var(--ink); line-height: 56px;
  }
  .sheet-rule { position: absolute; left: 17px; top: 64px; width: 866px; height: 1px; background: var(--ink); }

  .section-band {
    position: absolute; left: 0; width: 901px; height: 43px; background: var(--ink);
    color: var(--paper); font-family: "Didact Gothic", sans-serif; font-size: 42px;
    line-height: 46px; text-align: right; padding-right: 2px; letter-spacing: 1px;
  }
  .section-band--front { top: 215px; }
  .section-band--back { top: 766px; }

  .label { position: absolute; }
  .label--red { background: var(--label-dark); }
  .label--white { background: var(--label-light); }

  .brand-name { position: absolute; left: 0; width: 100%; text-align: center; line-height: 1; }
  .label--red .brand-name { color: var(--paper); }
  .label--white .brand-name { color: var(--type-dark); }

  .front-label { top: 289px; width: 365px; height: 428px; }
  .front-label .brand-name { top: 290px; top: 4px; font-size: 168px; letter-spacing: -6px; }

  .frame { position: absolute; }
  .frame-text { position: absolute; left: 0; width: 100%; text-align: center; line-height: 1; }

  .back-label { top: 833px; width: 280px; height: 367px; }
  .back-label .brand-name { top: 6px; font-size: 56px; letter-spacing: -2px; }
  .back-variety { position: absolute; left: 0; width: 100%; text-align: center; top: 66px; font-size: 19px; }
  .back-vintage { position: absolute; left: 0; width: 100%; text-align: center; top: 96px; font-size: 19px; }
  .label--red .back-variety, .label--red .back-vintage { color: #d9d9d9; }
  .label--white .back-variety, .label--white .back-vintage { color: var(--type-muted); }

  .spec { position: absolute; font-family: "PT Sans Narrow", sans-serif; line-height: 1; }
  .label--red .spec { color: var(--paper); }
  .label--white .spec { color: var(--type-dark); }
  .spec--alc { left: 10px; top: 135px; font-size: 17px; }
  .spec--volume { right: 15px; top: 133px; font-size: 19px; }
  .spec--drinks { left: 14px; top: 160px; font-size: 11px; }
  .spec--sulphites { right: 15px; top: 160px; font-size: 11px; }
  .spec--allergen { left: 0; width: 100%; text-align: center; top: 270px; font-size: 10px; }
  .spec-rule { position: absolute; left: 10px; width: 255px; height: 1px; }
  .label--red .spec-rule { background: #bfbfbf; }
  .label--white .spec-rule { background: #555555; }
  .description-frame { position: absolute; left: 18px; top: 179px; width: 239px; height: 81px; }
  .description-area { position: absolute; left: 8px; top: 8px; width: 223px; height: 64px; }
  .gi { position: absolute; left: 0; width: 100%; text-align: center; top: 345px; font-size: 17px; }
  .label--red .gi { color: #d9d9d9; }
  .label--white .gi { color: var(--type-muted); }
</style>
</head>
<body>
<main class="sheet">
  <h1 class="sheet-title">PACKAGING DESIGN: wine label for L&amp;T</h1>
  <div class="sheet-rule"></div>

  <div class="section-band section-band--front">FRONT LABELS</div>

  <!-- Pinot Noir front -->
  <section class="label label--red front-label" style="left:30px;">
    <div class="brand-name">L&amp;T</div>
    <div class="frame" style="left:12px;top:169px;width:341px;height:252px;background:var(--grey-mid);"></div>
    <div class="frame" style="left:33px;top:188px;width:295px;height:214px;background:var(--grey-soft);"></div>
    <div class="frame" style="left:61px;top:207px;width:240px;height:175px;background:var(--grey-pale);"></div>
    <div class="frame" style="left:78px;top:224px;width:205px;height:143px;background:var(--grey-mist);"></div>
    <div class="frame-text" style="top:230px;font-size:24px;color:var(--ink);">PINOT NOIR</div>
    <div class="frame-text" style="top:315px;font-size:23px;color:var(--ink);">2012</div>
    <div class="frame-text" style="top:370px;font-size:18px;color:var(--ink);">YARRA VALLEY</div>
  </section>

  <!-- Sauvignon Blanc front -->
  <section class="label label--white front-label" style="left:509px;">
    <div class="brand-name">L&amp;T</div>
    <div class="frame" style="left:11px;top:169px;width:341px;height:253px;background:var(--grey-pale);"></div>
    <div class="frame" style="left:34px;top:187px;width:295px;height:215px;background:var(--grey-soft);"></div>
    <div class="frame" style="left:61px;top:207px;width:240px;height:174px;background:var(--grey-mid);"></div>
    <div class="frame" style="left:80px;top:224px;width:202px;height:142px;background:var(--grey-deep);"></div>
    <div class="frame-text" style="top:227px;font-size:22px;line-height:27px;color:var(--paper);">SAUVIGNON<br>BLANC</div>
    <div class="frame-text" style="top:298px;font-size:22px;color:var(--paper);">2012</div>
    <div class="frame-text" style="top:348px;font-size:17px;color:var(--paper);">YARRA VALLEY</div>
    <div class="frame-text" style="top:405px;font-size:15px;color:var(--type-muted);">WINE OF AUSTRALIA</div>
  </section>

  <div class="section-band section-band--back">BACK LABELS</div>

  <!-- Pinot Noir back -->
  <section class="label label--red back-label" style="left:127px;">
    <div class="brand-name">L&amp;T</div>
    <div class="back-variety">PINOT NOIR</div>
    <div class="back-vintage">2012</div>
    <div class="spec spec--alc">12,5%ALC/VOL</div>
    <div class="spec spec--volume">750 mL</div>
    <div class="spec-rule" style="top:154px;"></div>
    <div class="spec spec--drinks">Approx.7.8 standard drinks</div>
    <div class="spec spec--sulphites">Sulphites added.</div>
    <div class="description-frame" style="background:var(--grey-soft);">
      <div class="description-area" style="background:#e8e8e8;"></div>
    </div>
    <div class="spec spec--allergen">Fined with the aid of egg and milk products and traces may remain.</div>
    <div class="spec-rule" style="top:281px;"></div>
    <div class="gi">WINE OF AUSTRALIA</div>
  </section>

  <!-- Sauvignon Blanc back -->
  <section class="label label--white back-label" style="left:507px;">
    <div class="brand-name">L&amp;T</div>
    <div class="back-variety">SAUVIGNON BLANC</div>
    <div class="back-vintage">2012</div>
    <div class="spec spec--alc">12,5%ALC/VOL</div>
    <div class="spec spec--volume">750 mL</div>
    <div class="spec-rule" style="top:154px;"></div>
    <div class="spec spec--drinks">Approx.7.8 standard drinks</div>
    <div class="spec spec--sulphites">Sulphites added.</div>
    <div class="description-frame" style="background:var(--grey-pale);">
      <div class="description-area" style="background:var(--grey-mid);"></div>
    </div>
    <div class="spec spec--allergen">Fined with the aid of egg and milk products and traces may remain.</div>
    <div class="spec-rule" style="top:281px;"></div>
    <div class="gi">WINE OF AUSTRALIA</div>
  </section>
</main>
</body>
</html>
```